A Writer With A Website (Writes action/mysteries with a touch of romance thrown in)

I need a website. I am an unpublished writer. I own a domain and tried a bit to design one in Wordpress. I would like to be able to change out pictures, blog, and receive email. My fav color is orange (but not necessary in website) I like the font "Hello Stockholm" Probably 4 or five different pages. Attached is a poor scan of a business card.
Updates

Had a recent death in the family, my inspiration to get the site designed and also the reason I may need a few days.

I write books action mysteries. So far all take place in Wyoming. I realize there was not much info given. Pages: Home, Looking for representation, recommended reading and other things I like, Mirabel (a page dedicated to my daughter who just passed away), and other useful links. Probably shorter ways to say those, but you get the idea.

Thanks for the designs submitted. I know I gave very little direction. There are a few authors who write in Wyoming who are popular, RT Haskell, Dwight Fenner (Ashcroft Saga) I would argue that the main character in any of their books is Wyoming, or the West. No cliches. Cowboy hats, horses, not so good. For those outside the US, maybe do a serch on Wyoming and look at the pictures. I have photo's for possible use in my design, will post them tonight. Thanks all. -k-

I am not sure how much info gets added, how much the designer does and how I fill in the "blanks". Here is partial text for the "Mirabel" page: Over the years, our daughters’ friends overlapped one another and two or three became like daughters to Loreen and me. Some even became our friends as they grew into adulthood. One had a father who tried to committed suicide multiple times. After one attempt she asked him, “why?” He said, “I am glad you can’t understand why, only someone who can travel to that dark a place can understand why”. He was eventually successful. She shared that story with us on August 14th when our daughter Mirabel found that dark place in herself and took her life. We found a suicide note, then her body, then everything went into a fog. An hour or so later, my wife and I stood on the front lawn after the police interviews and watched as the corner slide a covered corpse into the white SUV with darkened windows. We stood there as the rain began to fall, and the sky sobbed with us. As they closed the back of the coroner’s Suburban, the rain fell harder and harder and a fireman guided us back into the house that will never be the same for us.

Target Market(s)

Currently trying to get an agent, this is to look like I have followers.

Number of Pages Required

5+ page

Font styles to use
Serif

Colors
f68e4e

Requirements
Nice to have
• I like orange (more of a burnt orange color) I am a big fan of Matthias Dorrel. A "feel" like that might be nice. I am from Wyoming, That rugged western culture shows up in all my writing.
Should not have
• Western Cliche,

```html
<!DOCTYPE html>
<html lang="en">
<head>
<meta charset="utf-8">
<title>R L Hartwell — Author</title>
<link href="https://fonts.googleapis.com/css2?family=Allura&family=Libre+Baskerville&family=Roboto+Condensed:wght@500&display=swap" rel="stylesheet">
<style>
:root{
  --orange:#f68e4e;
  --ink:#111;
  --white:#fff;
  --bar:#000;
  --paper:#f7f6f5;
}
*{margin:0;padding:0;box-sizing:border-box}
html,body{width:1160px;height:1200px;overflow:hidden;background:var(--white)}
body{position:relative;font-family:"Libre Baskerville",Georgia,serif;color:var(--ink)}
.topbar{position:absolute;top:0;left:0;width:1160px;height:24px;background:var(--bar);color:var(--white);
  font-family:"Roboto Condensed",Arial,sans-serif;font-weight:500;font-size:11px;display:flex;justify-content:space-between;align-items:center;padding:0 18px 0 42px}
.header{position:absolute;top:24px;left:0;width:1160px;height:80px;background:var(--white);display:flex;align-items:center}
.brand{position:absolute;left:42px;font-size:30px;color:var(--orange);letter-spacing:1px}
.nav{position:absolute;left:492px;display:flex;gap:25px;font-size:13.5px;letter-spacing:.3px}
.nav span{display:flex;align-items:center;gap:3px}
.nav svg{width:8px;height:6px}
.tools{position:absolute;right:18px;display:flex;gap:12px;align-items:center}
.hero{position:absolute;top:104px;left:0;width:1160px;height:560px;
  background:radial-gradient(ellipse 420px 300px at 590px 430px,#f6b14f 0%,#e07a1e 35%,rgba(160,70,20,.0) 75%),
  linear-gradient(180deg,#5f4a3a 0%,#b87640 30%,#d98a3a 55%,#7a3412 80%,#3a1408 100%)}
.hero-bg{position:absolute;inset:0}
.hero-title{position:absolute;top:82px;width:100%;text-align:center;font-family:"Allura",cursive;font-weight:400;font-size:104px;color:var(--white);line-height:1}
.hero-sub{position:absolute;top:264px;width:100%;text-align:center;font-size:13.5px;color:var(--ink)}
.hero-name{position:absolute;top:322px;width:100%;text-align:center;font-size:40px;color:var(--white);letter-spacing:1px}
.order{position:absolute;top:443px;left:508px;display:flex;height:28px}
.order .label{background:var(--orange);color:var(--white);font-size:15px;padding:0 10px;display:flex;align-items:center}
.order .arrow{background:var(--white);width:24px;display:flex;align-items:center;justify-content:center}
.stats-section{position:absolute;top:664px;left:0;width:1160px;height:306px;
  background:linear-gradient(100deg,#f4f4f4 0%,#f8f8f8 45%,#ece8e4 62%,#c98d76 80%,#d99a84 100%)}
.stats-section .band{position:absolute;top:0;left:0;width:100%;height:27px;background:rgba(235,235,235,.7)}
.stats{position:absolute;top:44px;left:0;width:100%}
.stat{position:absolute;width:200px;text-align:center;color:var(--orange)}
.stat svg{display:block;margin:0 auto;width:40px;height:40px}
.stat .num{font-size:42px;line-height:1;margin-top:4px}
.stat .label{font-size:14.5px;letter-spacing:.3px;margin-top:4px}
.books-heading{position:absolute;top:218px;width:100%;text-align:center;font-family:"Allura",cursive;font-weight:400;font-size:50px;color:var(--ink)}
.book-grid{position:absolute;top:970px;left:0;width:1160px;height:192px;display:flex}
.book-photo{flex:1;height:192px}
.book-photo.one{background:linear-gradient(180deg,#b7b1a6 0%,#8e7a62 45%,#ece6dd 100%)}
.book-photo.two{background:linear-gradient(180deg,#a9acae 0%,#c39a5c 40%,#b9752c 100%)}
.book-photo.three{background:linear-gradient(180deg,#d9dcdc 0%,#c7bfb0 50%,#b3906a 100%)}
.book-titles{position:absolute;top:1162px;left:0;width:1160px;height:38px;display:flex;
  background:linear-gradient(90deg,#f8f8f8 0%,#f4f2f0 65%,#dfb7a6 85%,#c98d76 100%)}
.book-titles span{flex:1;text-align:center;padding-top:20px;font-size:15.5px;letter-spacing:.2px}
</style>
</head>
<body>
<div class="topbar"><span>hello@ridgeline-press.com</span><span>+1 307 555 0148</span></div>

<header class="header">
  <div class="brand">R L Hartwell</div>
  <nav class="nav">
    <span>HOME<svg viewBox="0 0 8 6"><path d="M1 1l3 3 3-3" fill="none" stroke="#111" stroke-width="1.3"/></svg></span>
    <span>ABOUT<svg viewBox="0 0 8 6"><path d="M1 1l3 3 3-3" fill="none" stroke="#111" stroke-width="1.3"/></svg></span>
    <span>STORE<svg viewBox="0 0 8 6"><path d="M1 1l3 3 3-3" fill="none" stroke="#111" stroke-width="1.3"/></svg></span>
    <span>BOOKS<svg viewBox="0 0 8 6"><path d="M1 1l3 3 3-3" fill="none" stroke="#111" stroke-width="1.3"/></svg></span>
    <span>STORE<svg viewBox="0 0 8 6"><path d="M1 1l3 3 3-3" fill="none" stroke="#111" stroke-width="1.3"/></svg></span>
    <span style="margin-left:4px">CONTACT</span>
  </nav>
  <div class="tools">
    <svg width="24" height="24" viewBox="0 0 24 24"><circle cx="10" cy="10" r="7" fill="none" stroke="#111" stroke-width="2.6"/><path d="M15 15l7 7" stroke="#111" stroke-width="3"/></svg>
    <svg width="24" height="18" viewBox="0 0 24 18"><path d="M0 2h24M0 9h24M0 16h24" stroke="#111" stroke-width="2.6"/></svg>
  </div>
</header>

<section class="hero">
  <div class="hero-bg" role="img" aria-label="Mountain valley with a misty river and pine forest at golden sunrise"></div>
  <h1 class="hero-title">prairie my last light</h1>
  <p class="hero-sub">the latest book by</p>
  <p class="hero-name">R L Hartwell</p>
  <div class="order">
    <span class="label">ORDER NOW</span>
    <span class="arrow"><svg width="16" height="14" viewBox="0 0 16 14"><path d="M1 7h13M8 1l6 6-6 6" fill="none" stroke="#111" stroke-width="2"/></svg></span>
  </div>
</section>

<section class="stats-section" role="img" aria-label="Close-up of a hand holding a pencil over white paper">
  <div class="band"></div>
  <div class="stats">
    <div class="stat" style="left:262px">
      <svg viewBox="0 0 40 40"><circle cx="20" cy="11" r="8" fill="#f68e4e"/><path d="M3 40c0-12 7-18 17-18s17 6 17 18z" fill="#f68e4e"/></svg>
      <div class="num">112</div><div class="label">SOLD BOOKS</div>
    </div>
    <div class="stat" style="left:475px">
      <svg viewBox="0 0 40 40"><circle cx="20" cy="21" r="18" fill="#f68e4e"/><path d="M12 21l6 6 11-13" fill="none" stroke="#fff" stroke-width="3"/><path d="M20 3v5" stroke="#fff" stroke-width="2"/></svg>
      <div class="num">112</div><div class="label">RADIO TIME</div>
    </div>
    <div class="stat" style="left:692px">
      <svg viewBox="0 0 40 40"><circle cx="20" cy="8" r="6" fill="#f68e4e"/><path d="M5 38c0-14 6-22 15-22s15 8 15 22z" fill="#f68e4e"/><path d="M16 17l4 5 4-5M20 22v10" fill="none" stroke="#fff" stroke-width="2"/></svg>
      <div class="num">112</div><div class="label">SUCCESFUL TALKS</div>
    </div>
  </div>
  <h2 class="books-heading">books</h2>
</section>

<div class="book-grid">
  <div class="book-photo one" role="img" aria-label="Woman in a wide-brim hat in a frosty meadow"></div>
  <div class="book-photo two" role="img" aria-label="Woman sitting in golden grassland below hills"></div>
  <div class="book-photo three" role="img" aria-label="Woman holding her hat in a pale winter field"></div>
</div>
<div class="book-titles"><span>BOOK TITLE</span><span>BOOK TITLE</span><span>BOOK TITLE</span></div>
</body>
</html>
```